4' x 8' Construction Project Sign, think of a very large business card

We need project signs for our construction sites, the sign will be mounted along the road so cars driving by can quickly read. the sign should be able to be read as cars drive by doing highway speed.

Think like your making a large business card

I would like to include "NOW HIRING" Superintendents, Project Managers, Pipe Foremen, Pipe Layers, and Equipment Operators

Description of services we provide should include

Civil Construction Services
Land Clearing
Excavation
Underground Utilities
Environmental Maintenance

The 2 objectives is to market to future clients and to recruit new employees

The sign will be mounted on posts at the entrance of our construction projects
Updates

Low design quality

Target Market(s)

Construction and land developers

Industry/Entity Type

Construction Company

Other font styles liked:
• Hypatia Sans Pro lite

Colors

Designer to choose colors to be used in the design.

Requirements
Must have
• Clean and easy to read
• Civil Construction Services
• Land Clearing
• Excavation
• Underground Utilities
• Road Construction

```html
<!DOCTYPE html>
<html lang="en">
<head>
<meta charset="utf-8">
<title>Project Sign – Now Hiring</title>
<link href="https://fonts.googleapis.com/css2?family=Alegreya+Sans:wght@400;500;800&display=swap" rel="stylesheet">
<style>
  :root {
    --sign-blue: #3a4c8c;
    --sign-blue-deep: #2f3f7a;
    --sign-blue-light: #4560a8;
    --rule-blue: #5b70b3;
    --accent-blue: #5f7cd0;
    --divider-blue: #2c44a8;
    --band-grey: #5d5d62;
    --band-white: #ffffff;
    --text-white: #ffffff;
    --text-grey: #4f4f55;
    --art-dark: #141a40;
    --art-mid: #1f2a5e;
  }
  * { margin: 0; padding: 0; box-sizing: border-box; }
  html, body { width: 1200px; height: 840px; overflow: hidden; background: #e6e6e8; }
  .sign {
    position: relative;
    width: 1200px;
    height: 840px;
    font-family: "Alegreya Sans", sans-serif;
  }
  .sign-panel {
    position: absolute;
    left: 0; top: 0;
    width: 1200px; height: 683px;
    background: radial-gradient(ellipse at 72% 45%, var(--sign-blue-light) 0%, var(--sign-blue) 45%, var(--sign-blue-deep) 100%);
    overflow: hidden;
  }
  .headline {
    position: absolute;
    left: 78px; top: 62px;
    color: var(--text-white);
    font-weight: 800;
    font-size: 84px;
    line-height: 86px;
    letter-spacing: 1px;
    text-shadow: 3px 4px 8px rgba(0,0,0,0.35);
  }
  .headline-marker {
    position: absolute;
    left: 403px; top: 168px;
  }
  .roles {
    position: absolute;
    left: 78px; top: 254px;
    width: 432px;
    list-style: none;
  }
  .roles li {
    color: var(--text-white);
    font-size: 48px;
    font-weight: 400;
    line-height: 1;
    height: 73px;
    padding-top: 12px;
    border-bottom: 2px solid var(--rule-blue);
    white-space: nowrap;
  }
  .head-artwork {
    position: absolute;
    left: 630px; top: 10px;
    width: 420px; height: 540px;
    background: radial-gradient(ellipse 50% 50% at 50% 50%, var(--art-dark) 0%, var(--art-mid) 55%, rgba(58,76,140,0) 100%);
  }
  .company {
    position: absolute;
    left: 655px; top: 562px;
    display: flex;
    align-items: center;
    gap: 22px;
    color: var(--text-white);
    font-weight: 800;
  }
  .company-square {
    width: 76px; height: 76px;
    border: 6px solid var(--text-white);
  }
  .company-name {
    font-size: 40px;
    line-height: 40px;
    letter-spacing: 0.5px;
  }
  .company-name span { display: block; font-size: 21px; letter-spacing: 6.5px; line-height: 30px; }
  .band-strip {
    position: absolute;
    left: 0; top: 683px;
    width: 1200px; height: 17px;
    background: var(--band-grey);
  }
  .services {
    position: absolute;
    left: 0; top: 700px;
    width: 1200px; height: 140px;
    background: var(--band-white);
    display: flex;
    flex-direction: column;
    align-items: center;
    justify-content: center;
    gap: 10px;
  }
  .services-row {
    display: flex;
    list-style: none;
  }
  .services-row li {
    color: var(--text-grey);
    font-size: 33px;
    font-weight: 500;
    padding: 0 20px;
    border-left: 3px solid var(--divider-blue);
    line-height: 42px;
    white-space: nowrap;
  }
  .services-row li:first-child { border-left: none; }
</style>
</head>
<body>
  <main class="sign">
    <section class="sign-panel">
      <h1 class="headline">NOW<br>HIRING!</h1>
      <svg class="headline-marker" width="48" height="50" viewBox="0 0 48 50" aria-hidden="true">
        <polygon points="0,0 48,0 24,50" fill="var(--accent-blue)"/>
      </svg>
      <ul class="roles">
        <li>Superintendents</li>
        <li>Project Managers</li>
        <li>Pipe Foremen</li>
        <li>Pipe Layers</li>
        <li>Equipment Operators</li>
      </ul>
      <div class="head-artwork" role="img" aria-label="Silhouette of a head in profile filled with construction workers, scaffolding and cranes"></div>
      <div class="company">
        <div class="company-square"></div>
        <div class="company-name">HARLOW RIDGE<span>CIVIL CONSTRUCTION</span></div>
      </div>
    </section>
    <div class="band-strip"></div>
    <footer class="services">
      <ul class="services-row">
        <li>Civil Construction Services</li>
        <li>Land Clearing</li>
        <li>Excavation</li>
      </ul>
      <ul class="services-row">
        <li>Underground Utilities</li>
        <li>Road Construction</li>
        <li>Environmental Maintenance</li>
      </ul>
    </footer>
  </main>
</body>
</html>
```